Lanterns After Rain - CD cover indie music

This is my 4th and final album. I am sharing my story of trials, pain and persistence that led me here, like a sound track to a short film.
I would like a design that communicates both a painful phase of life, yet tranquility and beauty found as life winds down. Can be illustrated or photograph.
On front design should have title 'Lanterns After Rain' and artist name.
I will need to add credits and song list.
I am thinking a booklet will be added with lyrics and a few photos and plan to work with this artist. Thank you

Target Market(s)

Folk, easy listening, story telling

Industry/Entity Type

Indie music - independent

Font styles to use
Sans Serif
Other font styles liked:
• I like also verdana font.

Requirements
Nice to have
• a contrast of colors to emotions may work well. There is a portuguese word ‘saudade’ that expresses sadness, but longing also.
Should not have
• No bright red. Not busy. No images of people or animals.

```html
<!DOCTYPE html>
<html lang="en">
<head>
<meta charset="UTF-8">
<title>Lanterns After Rain – Album Cover</title>
<link href="https://fonts.googleapis.com/css2?family=Nothing+You+Could+Do&display=swap" rel="stylesheet">
<style>
  :root {
    --page: #ffffff;
    --frame-edge: #d9d6cf;
    --mist: #ebe5e6;
    --orange: #f0a064;
    --cream: #f2e6d4;
    --lavender: #dcd0dc;
    --lilac-grey: #c9c2cc;
    --olive: #d6d2a8;
    --sage: #b9c8a8;
    --leaf: #6f9e63;
    --title: #ffffff;
  }
  html, body {
    margin: 0;
    padding: 0;
    width: 1200px;
    height: 849px;
    overflow: hidden;
    background: var(--page);
  }
  .canvas {
    position: relative;
    width: 1200px;
    height: 849px;
    background: var(--page);
  }
  .cover {
    position: absolute;
    left: 291px;
    top: 118px;
    width: 594px;
    height: 595px;
    box-shadow: 0 0 0 0.6px var(--frame-edge);
    overflow: hidden;
  }
  .cover-artwork {
    position: absolute;
    inset: 0;
    background:
      radial-gradient(ellipse 10% 22% at 4% 38%, var(--orange) 0%, rgba(240,160,100,0) 100%),
      radial-gradient(ellipse 22% 30% at 12% 35%, rgba(238,185,143,0.7) 0%, rgba(238,185,143,0) 100%),
      radial-gradient(ellipse 18% 22% at 37% 28%, var(--cream) 0%, rgba(242,230,212,0) 100%),
      radial-gradient(ellipse 14% 14% at 33% 42%, rgba(239,200,200,0.8) 0%, rgba(239,200,200,0) 100%),
      radial-gradient(ellipse 8% 14% at 68% 16%, var(--olive) 0%, rgba(214,210,168,0) 100%),
      radial-gradient(ellipse 14% 30% at 70% 30%, rgba(201,186,205,0.9) 0%, rgba(201,186,205,0) 100%),
      radial-gradient(ellipse 14% 40% at 86% 35%, var(--lilac-grey) 0%, rgba(201,194,204,0) 100%),
      radial-gradient(ellipse 10% 28% at 90% 76%, var(--leaf) 0%, rgba(111,158,99,0) 100%),
      radial-gradient(ellipse 22% 40% at 86% 82%, var(--sage) 0%, rgba(185,200,168,0) 100%),
      radial-gradient(ellipse 30% 26% at 14% 88%, rgba(220,204,218,0.9) 0%, rgba(220,204,218,0) 100%),
      radial-gradient(ellipse 40% 50% at 40% 65%, var(--lavender) 0%, rgba(220,208,220,0) 100%),
      linear-gradient(180deg, var(--mist) 0%, #e6dfe2 60%, #e8e3e2 100%);
    filter: blur(6px);
    transform: scale(1.04);
  }
  .cover-title {
    position: absolute;
    left: 0;
    right: 0;
    top: 484px;
    margin: 0;
    text-align: center;
    font-family: "Nothing You Could Do", cursive;
    font-weight: 400;
    font-size: 38px;
    color: var(--title);
    letter-spacing: 0.5px;
    line-height: 1;
    white-space: nowrap;
  }
  .cover-artist {
    position: absolute;
    left: 0;
    right: 0;
    top: 548px;
    margin: 0;
    text-align: center;
    font-family: "Nothing You Could Do", cursive;
    font-weight: 400;
    font-size: 18px;
    color: var(--title);
    letter-spacing: 1px;
    line-height: 1;
    white-space: nowrap;
  }
  .title-underline {
    position: absolute;
    left: 0;
    top: 0;
    width: 594px;
    height: 595px;
    pointer-events: none;
  }
</style>
</head>
<body>
  <div class="canvas">
    <div class="cover">
      <div class="cover-artwork" role="img" aria-label="Soft, out-of-focus photograph of flowers in peach, cream, lavender and green tones"></div>
      <h1 class="cover-title">Lanterns After Rain</h1>
      <svg class="title-underline" viewBox="0 0 594 595" aria-hidden="true">
        <path d="M117 538 C 200 529, 300 539, 360 539 S 450 531, 466 536" fill="none" stroke="#ffffff" stroke-width="1.3" stroke-linecap="round"/>
      </svg>
      <p class="cover-artist">Elena Voss</p>
    </div>
  </div>
</body>
</html>
```